Vemtra Group: Business Card for a high end technology company

We need a cool new design for our business cards using our cloud logo. We are a technology consulting business. We pride ourselves on be the best of the best. We mainly focus on cloud solutions and managed services. We need a business card that sets us apart from the other technology companies in the area and allows us to stand out.

Target Market(s)

Technology departments, CIO, CEOs, and Information Technology Staff.

Industry/Entity Type

Information Technology

Contact Information for Business Card

Must have the logo and our name.
Must have employee name, email address, office phone, cell phone and website.
Need to have all info on one side a cool design on backside.

Font styles to use
Serif
Sans Serif

Requirements
Must have
• Must have the logo and our name.
• Must have employee name, email address, office phone, cell phone and website.
• Need to have all info on one side a cool design on back side.
• Must be a crisp clean design, not too busy or confusing.

```html
<!DOCTYPE html>
<html lang="en">
<head>
<meta charset="utf-8">
<title>Vemtra Group Business Card</title>
<link rel="stylesheet" href="https://fonts.googleapis.com/css2?family=Open+Sans:wght@400;600;700&display=swap">
<style>
  :root {
    --page-bg: #e9ecef;
    --card-white: #ffffff;
    --card-fade: #eef1f4;
    --brand-blue: #1d8fdc;
    --brand-blue-light: #5cb6ee;
    --brand-blue-deep: #1a5d9c;
    --ink: #333a40;
    --ink-soft: #4a5158;
    --white: #ffffff;
  }
  * { margin: 0; padding: 0; box-sizing: border-box; }
  html, body { width: 1200px; height: 950px; overflow: hidden; }
  body {
    background: var(--page-bg);
    font-family: "Open Sans", Arial, sans-serif;
    display: flex;
    flex-direction: column;
    align-items: center;
    justify-content: center;
    gap: 60px;
  }
  .card {
    position: relative;
    width: 700px;
    height: 400px;
    border-radius: 4px;
    overflow: hidden;
    box-shadow: 0 6px 18px rgba(0,0,0,0.18);
  }

  /* Front */
  .card-front {
    background: linear-gradient(180deg, var(--card-white) 0%, var(--card-white) 70%, var(--card-fade) 100%);
  }
  .brand {
    position: absolute;
    left: 44px;
    top: 52px;
    display: flex;
    align-items: center;
    gap: 14px;
  }
  .brand-dot {
    width: 46px; height: 46px;
    border-radius: 50%;
    background: var(--brand-blue);
  }
  .brand-name {
    font-size: 34px;
    font-weight: 600;
    color: var(--ink);
    letter-spacing: 0.5px;
  }
  .brand-url {
    position: absolute;
    left: 104px;
    top: 104px;
    font-size: 11px;
    font-weight: 700;
    color: var(--ink);
  }
  .name-band {
    position: absolute;
    left: 0; right: 0;
    top: 140px;
    height: 66px;
    background: linear-gradient(90deg, var(--brand-blue) 0%, var(--brand-blue) 55%, var(--brand-blue-light) 70%, var(--brand-blue) 85%, var(--brand-blue) 100%);
    padding: 8px 0 0 44px;
    color: var(--white);
  }
  .person-name { font-size: 22px; font-weight: 700; line-height: 1.2; }
  .person-title { font-size: 15px; font-weight: 400; line-height: 1.4; }
  .band-mark {
    position: absolute;
    right: 70px;
    top: 9px;
    width: 48px; height: 48px;
    border-radius: 50%;
    background: rgba(255,255,255,0.85);
  }
  .phones {
    position: absolute;
    left: 44px;
    top: 232px;
    list-style: none;
  }
  .contact-line {
    display: flex;
    align-items: center;
    gap: 10px;
    font-size: 17px;
    color: var(--ink-soft);
    line-height: 28px;
  }
  .web-details {
    position: absolute;
    right: 44px;
    bottom: 38px;
    list-style: none;
  }
  .web-details .contact-line { justify-content: flex-end; }
  .icon { width: 16px; height: 16px; flex: none; }

  /* Back */
  .card-back {
    background: linear-gradient(120deg, var(--brand-blue) 0%, #2a7fc6 55%, var(--brand-blue-deep) 100%);
    display: flex;
    flex-direction: column;
    align-items: center;
    justify-content: center;
    color: var(--white);
  }
  .back-brand { display: flex; align-items: center; gap: 18px; }
  .back-brand .brand-dot { width: 60px; height: 60px; background: var(--white); }
  .back-brand .brand-name { color: var(--white); font-size: 44px; }
  .back-url { margin-top: 10px; font-size: 14px; font-weight: 700; }
</style>
</head>
<body>

<section class="card card-front" aria-label="Business card front">
  <div class="brand">
    <span class="brand-dot"></span>
    <span class="brand-name">Vemtra Group</span>
  </div>
  <div class="brand-url">www.vemtragroup.com</div>

  <div class="name-band">
    <div class="person-name">Marcus Hale</div>
    <div class="person-title">President</div>
    <span class="band-mark"></span>
  </div>

  <ul class="phones">
    <li class="contact-line">
      <svg class="icon" viewBox="0 0 16 16" aria-hidden="true"><path fill="#1d8fdc" d="M3.5 1.5l2.2 2.6-1.3 1.6c.9 2 2.3 3.5 4.1 4.5l1.6-1.3 2.6 2.2-1.2 2.2C6.9 13 3 9.1 2.3 2.7z"/></svg>
      555 0142 7781
    </li>
    <li class="contact-line">
      <svg class="icon" viewBox="0 0 16 16" aria-hidden="true"><rect x="4" y="1" width="8" height="14" rx="1.5" fill="#1d8fdc"/><rect x="5.3" y="2.8" width="5.4" height="9" fill="#fff"/></svg>
      555 0198 3364
    </li>
  </ul>

  <ul class="web-details">
    <li class="contact-line">
      marcus@vemtragroup.com
      <svg class="icon" viewBox="0 0 16 16" aria-hidden="true"><rect x="1" y="3.5" width="14" height="9" fill="#1d8fdc"/><path d="M1.5 4l6.5 5 6.5-5" fill="none" stroke="#fff" stroke-width="1.2"/></svg>
    </li>
    <li class="contact-line">
      www.vemtragroup.com
      <svg class="icon" viewBox="0 0 16 16" aria-hidden="true"><circle cx="8" cy="8" r="7" fill="#1d8fdc"/><path d="M1 8h14M8 1c-3 3.5-3 10.5 0 14M8 1c3 3.5 3 10.5 0 14" fill="none" stroke="#fff" stroke-width="1"/></svg>
    </li>
  </ul>
</section>

<section class="card card-back" aria-label="Business card back">
  <div class="back-brand">
    <span class="brand-dot"></span>
    <span class="brand-name">Vemtra Group</span>
  </div>
  <div class="back-url">www.vemtragroup.com</div>
</section>

</body>
</html>
```